Cedarbrook Lane Allies Stationery

Use attached logo for stationery
Stationery, Letterhead and Envelope + Business cards

Tag line: Walking alongside those doing the work of the Gospel

```html
<!DOCTYPE html>
<html lang="en">
<head>
<meta charset="utf-8">
<title>Cedarbrook Lane Allies Stationery</title>
<link href="https://fonts.googleapis.com/css2?family=Open+Sans:wght@400;600;700&display=swap" rel="stylesheet">
<style>
  :root{
    --navy:#0b4f8a;
    --cyan:#62d9f4;
    --gold:#f7c21b;
    --ink:#4a4a4a;
    --paper:#ffffff;
    --backdrop:#e4e4e4;
  }
  *{box-sizing:border-box;margin:0;padding:0}
  html,body{width:979px;height:1200px;overflow:hidden}
  body{background:var(--backdrop);font-family:"Open Sans",Arial,sans-serif;color:var(--ink);position:relative}

  .letterhead{position:absolute;left:230px;top:22px;width:520px;height:735px;background:var(--paper);box-shadow:0 6px 18px rgba(0,0,0,.12);overflow:hidden}
  .brand-name{font-family:"Open Sans",Arial,sans-serif;font-weight:700;color:var(--navy);display:flex;align-items:center;gap:7px;letter-spacing:.02em;text-transform:uppercase}
  .brand-dot{border-radius:50%;background:var(--navy);flex:none}
  .letterhead .brand-name{position:absolute;left:44px;top:66px;font-size:15px}
  .letterhead .brand-dot{width:14px;height:14px}

  .contact-list{list-style:none;font-size:7px;line-height:10px;color:var(--ink)}
  .contact-list li{display:flex;align-items:center;gap:4px}
  .contact-list svg{width:6px;height:6px;fill:var(--navy);flex:none}
  .letterhead .contact-list{position:absolute;right:64px;top:30px}

  .letter-body{position:absolute;left:44px;top:132px;width:420px;font-size:8px;line-height:11px}
  .greeting{font-family:Arial,"Open Sans",sans-serif;font-weight:700;font-size:10px;color:#111;margin-bottom:10px}
  .letter-body p{margin-bottom:10px;text-align:justify}
  .signature{width:100px;height:36px;margin-top:18px;background:linear-gradient(90deg,#f2f2f2,#e2e2e2);border-radius:3px}

  .letter-footer{position:absolute;left:0;bottom:0;width:520px;height:190px}
  .letter-footer svg{position:absolute;inset:0;width:100%;height:100%}
  .footer-address{position:absolute;left:44px;bottom:26px;font-size:8px;line-height:11px;color:#fff}
  .footer-address strong{color:var(--gold);font-weight:700;display:block}

  .card{position:absolute;width:320px;height:183px;background:var(--paper);box-shadow:0 5px 14px rgba(0,0,0,.14);overflow:hidden}
  .card-info{left:170px;top:800px}
  .card-logo{left:470px;top:935px}

  .card-info .brand-name{position:absolute;left:22px;top:28px;font-size:11px}
  .card-info .brand-dot{width:10px;height:10px}
  .person{position:absolute;right:20px;top:20px;text-align:right}
  .person-name{font-size:9px;font-weight:700;color:var(--navy);text-transform:uppercase}
  .person-role{font-size:7px}
  .card-info .contact-list{position:absolute;right:20px;top:56px;font-size:6.5px;line-height:9px;text-align:right}
  .card-info .contact-list li{justify-content:flex-end}
  .card-waves{position:absolute;left:0;bottom:0;width:320px;height:110px}
  .card-address{position:absolute;left:20px;bottom:14px;font-size:7px;line-height:10px;color:#fff}

  .card-logo .brand-name{position:absolute;left:0;right:0;top:78px;justify-content:center;font-size:14px}
  .card-logo .brand-dot{width:13px;height:13px}
</style>
</head>
<body>

<section class="letterhead" aria-label="Letterhead">
  <div class="brand-name"><span class="brand-dot"></span>Cedarbrook Lane Allies</div>

  <ul class="contact-list">
    <li><svg viewBox="0 0 10 10"><path d="M2 0h2l1 3-1.5 1a6 6 0 0 0 2.5 2.5L7 5l3 1v2c0 1-1 2-2 2A8 8 0 0 1 0 2c0-1 1-2 2-2z"/></svg>555-210-4830</li>
    <li><svg viewBox="0 0 10 10"><rect x="2" y="0" width="6" height="10" rx="1"/></svg>800-555-0192</li>
    <li><svg viewBox="0 0 10 10"><path d="M0 2h10v6H0z"/></svg>hello@cedarbrooklane.org</li>
    <li><svg viewBox="0 0 10 10"><circle cx="5" cy="5" r="5"/></svg>www.cedarbrooklane.org</li>
  </ul>

  <div class="letter-body">
    <p class="greeting">Dear Mr. Ellis,</p>
    <p>Lorem Ipsum is simply dummy text of the printing and typesetting industry. Lorem Ipsum has been the industry's standard dummy text ever since the 1500s, when an unknown printer took a galley of type and scrambled it to make a type specimen book. It has survived not only five centuries, but also the leap into electronic typesetting, remaining essentially unchanged.</p>
    <p>The standard chunk of Lorem Ipsum used since the 1500s is reproduced below for those interested. Sections 1.10.32 and 1.10.33 from "de Finibus Bonorum et Malorum" by Cicero are also reproduced in their exact original form, accompanied by English versions from the 1914 translation by H. Rackham.</p>
    <p>Lorem Ipsum is simply dummy text of the printing and typesetting industry. Lorem Ipsum has been the industry's standard dummy text ever since the 1500s, when an unknown printer took a galley of type and scrambled it to make a type specimen book. It has survived not only five centuries, but also the leap into electronic typesetting, remaining essentially unchanged. It was popularised in the</p>
    <p>The standard chunk of Lorem Ipsum used since the 1500s is reproduced below for those interested. Sections 1.10.32 and 1.10.33 from "de Finibus Bonorum et Malorum" by Cicero are also reproduced in their exact original form, accompanied by English versions from the 1914 translation by H. Rackham.</p>
    <p>The standard chunk of Lorem Ipsum used since the 1500s is reproduced below for those interested. Sections 1.10.32 and 1.10.33 from "de Finibus Bonorum et Malorum" by Cicero are also reproduced in their exact original form.</p>
    <div class="signature" role="img" aria-label="Handwritten signature"></div>
  </div>

  <div class="letter-footer">
    <svg viewBox="0 0 520 190" preserveAspectRatio="none" aria-hidden="true">
      <path d="M0 190V110C140 70 330 150 520 20V190Z" fill="var(--navy)"/>
      <path d="M0 104C150 55 330 140 520 12" fill="none" stroke="var(--cyan)" stroke-width="9"/>
      <path d="M40 96C160 40 300 110 470 60C320 80 180 40 40 96Z" fill="var(--gold)"/>
    </svg>
    <div class="footer-address"><strong>Cedarbrook Lane Allies</strong>Po. box 201, Street Name, City Name, Zip Code - 00000</div>
  </div>
</section>

<section class="card card-info" aria-label="Business card, contact side">
  <div class="brand-name"><span class="brand-dot"></span>Cedarbrook Lane Allies</div>
  <div class="person">
    <div class="person-name">Morgan Hale</div>
    <div class="person-role">Project Manager</div>
  </div>
  <ul class="contact-list">
    <li>800-555-0192<svg viewBox="0 0 10 10"><path d="M2 0h2l1 3-1.5 1a6 6 0 0 0 2.5 2.5L7 5l3 1v2c0 1-1 2-2 2A8 8 0 0 1 0 2c0-1 1-2 2-2z"/></svg></li>
    <li>hello@cedarbrooklane.org<svg viewBox="0 0 10 10"><path d="M0 2h10v6H0z"/></svg></li>
    <li>www.cedarbrooklane.org<svg viewBox="0 0 10 10"><circle cx="5" cy="5" r="5"/></svg></li>
  </ul>
  <svg class="card-waves" viewBox="0 0 320 110" preserveAspectRatio="none" aria-hidden="true">
    <path d="M0 110V70C110 60 230 70 320 0V110Z" fill="var(--navy)"/>
    <path d="M0 66C110 56 230 66 320 -4" fill="none" stroke="var(--cyan)" stroke-width="6"/>
    <path d="M40 58C130 30 220 50 300 10C230 40 140 30 40 58Z" fill="var(--gold)"/>
  </svg>
  <div class="card-address">48 Willow Bend Road<br>Fairmont, TX 75000</div>
</section>

<section class="card card-logo" aria-label="Business card, name side">
  <div class="brand-name"><span class="brand-dot"></span>Cedarbrook Lane Allies</div>
</section>

</body>
</html>
```